Global Leadership Company requires banner design

I need 3 large banners designed. i will be using these for advertising and also a condensed version as the header on a splash pages.

I have attached the wording and also the photo's that i'd like used in each design.
Note: i've just placed the wording randomly, you'll have to place it where it makes the most sense for the message and the design.

I want something with bright colors that pops.

Reason: I'd like to give the most recent designers time to submit quality work.

```html
<!DOCTYPE html>
<html lang="en">
<head>
<meta charset="utf-8">
<title>Personal Empowerment Banner</title>
<link href="https://fonts.googleapis.com/css2?family=Oswald:wght@400;500;600;700&family=Roboto+Condensed:wght@400;700&display=swap" rel="stylesheet">
<style>
  :root {
    --red: #ee1c1c;
    --ink: #1d1d1b;
    --yellow: #f7e23a;
    --white: #ffffff;
    --orange: #f28c1a;
    --bar-light: #f4f4f4;
    --bar-dark: #cfcfcf;
    --burst-red: #d9302a;
    --burst-gold: #f3b23b;
    --portrait-warm: #f0a060;
    --portrait-skin: #e9c2a4;
  }
  html, body {
    margin: 0;
    padding: 0;
    overflow: hidden;
    background: var(--white);
  }
  .banner {
    position: relative;
    width: 1200px;
    height: 360px;
    overflow: hidden;
    background: var(--white);
    font-family: "Roboto Condensed", sans-serif;
    color: var(--ink);
  }
  .headline {
    position: absolute;
    left: 20px;
    top: 8px;
    margin: 0;
    font-family: "Oswald", sans-serif;
    font-weight: 600;
    font-size: 34px;
    line-height: 1.2;
    color: var(--red);
    white-space: nowrap;
    letter-spacing: -0.2px;
  }
  .subhead {
    position: absolute;
    left: 42px;
    top: 72px;
    margin: 0;
    font-family: "Oswald", sans-serif;
    font-weight: 400;
    font-size: 30px;
    white-space: nowrap;
  }
  .pitch {
    position: absolute;
    left: 55px;
    top: 126px;
    margin: 0;
    font-family: "Oswald", sans-serif;
    font-weight: 600;
    font-size: 29px;
    line-height: 49px;
    white-space: nowrap;
  }
  .pitch .light { font-weight: 400; }
  .burst {
    position: absolute;
    left: 700px;
    top: 68px;
    width: 165px;
    height: 150px;
  }
  .benefits {
    position: absolute;
    left: 0;
    top: 255px;
    width: 880px;
    height: 40px;
    padding: 0 30px 0 22px;
    box-sizing: border-box;
    background: var(--yellow);
    display: flex;
    justify-content: space-between;
    align-items: center;
    font-size: 19px;
    white-space: nowrap;
  }
  .launch {
    position: absolute;
    left: 200px;
    top: 311px;
    margin: 0;
    font-size: 19px;
    white-space: nowrap;
  }
  .launch .cta { color: var(--red); }
  .growth-chart {
    position: absolute;
    left: 1030px;
    top: 170px;
    width: 170px;
    height: 190px;
  }
  .portrait {
    position: absolute;
    left: 950px;
    top: 44px;
    width: 230px;
    height: 215px;
    border-radius: 90px 90px 30px 30px;
    background: radial-gradient(ellipse at 45% 30%, var(--portrait-skin) 0 30%, var(--portrait-warm) 62%, rgba(240,160,96,0) 72%);
  }
  .testimonial {
    position: absolute;
    left: 867px;
    top: 226px;
    width: 150px;
    height: 150px;
    border-radius: 50%;
    background: var(--red);
    color: var(--white);
    font-weight: 700;
    font-size: 14px;
    line-height: 1.22;
    text-align: center;
    display: flex;
    flex-direction: column;
    justify-content: center;
    padding: 0 14px;
    box-sizing: border-box;
  }
  .testimonial p { margin: 0; }
  .earnings {
    position: absolute;
    left: 1012px;
    top: 282px;
    margin: 0;
    font-family: "Oswald", sans-serif;
    font-weight: 700;
    font-size: 50px;
    line-height: 1;
    color: var(--red);
  }
</style>
</head>
<body>
<div class="banner">
  <h1 class="headline">WANTED - driven individuals READY to take their results to the next level.</h1>
  <h2 class="subhead">Personal Empowerment…..the NEXT Big Business</h2>
  <p class="pitch">“Let us show you how we’ve taught average people to<br>earn an executives salary from home <span class="light">– part time. FAST!”</span></p>

  <svg class="burst" viewBox="0 0 165 150" role="img" aria-label="Comic explosion burst illustration with the word BOOM">
    <defs>
      <radialGradient id="burstFill" cx="50%" cy="50%" r="50%">
        <stop offset="0%" stop-color="var(--burst-gold)"/>
        <stop offset="100%" stop-color="var(--burst-red)"/>
      </radialGradient>
    </defs>
    <ellipse cx="82" cy="75" rx="80" ry="72" fill="url(#burstFill)"/>
  </svg>

  <div class="benefits">
    <span>Make up to $5,000 per sale</span>
    <span>No cold calling</span>
    <span>No experience required</span>
    <span>No pressure selling</span>
    <span>NOT MLM</span>
  </div>

  <p class="launch">Just launched in United States <span class="cta">CLICK HERE FOR FREE INFO</span></p>

  <svg class="growth-chart" viewBox="0 0 170 190" aria-hidden="true">
    <defs>
      <linearGradient id="barShade" x1="0" x2="1">
        <stop offset="0%" stop-color="var(--bar-light)"/>
        <stop offset="100%" stop-color="var(--bar-dark)"/>
      </linearGradient>
    </defs>
    <rect x="8" y="150" width="18" height="40" fill="url(#barShade)"/>
    <rect x="32" y="130" width="18" height="60" fill="url(#barShade)"/>
    <rect x="56" y="112" width="18" height="78" fill="url(#barShade)"/>
    <rect x="80" y="88" width="18" height="102" fill="url(#barShade)"/>
    <rect x="104" y="62" width="18" height="128" fill="url(#barShade)"/>
    <rect x="128" y="36" width="18" height="154" fill="url(#barShade)"/>
    <rect x="150" y="14" width="18" height="176" fill="url(#barShade)"/>
    <polyline points="0,132 40,112 70,104 100,72 130,58 158,18" fill="none" stroke="var(--orange)" stroke-width="3"/>
    <polygon points="163,8 150,18 160,25" fill="var(--orange)"/>
  </svg>

  <div class="portrait" role="img" aria-label="Photo of a smiling woman in an orange top resting her chin on her hand"></div>

  <div class="testimonial">
    <p>“Within just 5 months I was making over $25,000 per month”</p>
    <p>Megan, Colorado</p>
  </div>

  <p class="earnings">$25,000</p>
</div>
</body>
</html>
```